依頼詳細
商品名:パームシュガー(ベトナム産)
容量:500g
デザイン:箱
添付している写真ファイル「包装」のように直径3.5cmの丸く固めたパームシュガーを数十個透明パックに入れて真空にして、箱に入れます。

サイズや文言などはPPTに記載しております。ベトナムでの販売が中心なので、日本語と英語、ベトナム語表記がありますが、英語とベトナム語は添付ファイル内にある文章をコピペしていただくだけです。

■裏面のデザインはほぼ不要

デザインのメインは表面と場合によって側面ちょっと。裏面は成分表や会社情報などが主なので、デザインはほぼなしで構いません。※文章はコピペ。

■イラスト&写真に関しまして

写真かイラストを入れていただきたいです。写真は法律で問題ないものをご使用くださいませ。弊社の方で持っている写真も添付します。

■ロゴに関しまして

弊社は現地では最近ネットなどで注目されているブランドです。できれば、ほどよくロゴを目立つようにしてください。

■デザインカラー

ロゴが水色(パステルカラー)なので、それに合わせた水色か、浅いピンクが希望です。

■納品形態
PNG、AI(アウトライン前と後をください)
■著作権
納品いただいた時点で弊社にわたるものとさせていただきます。

記載項目
サイズ:横11cm×高さ18.3cm×奥行2.6cm
詳細はPPT参照くださいませ。
希望イメージ
シンプル 複雑
単色 カラフル
暗い 明るい
日常 高級
遊び心 厳粛
未来的 伝統的
女性的 男性的
希望する色
赤系、水色系
納品ファイル
• イラストレーター形式 (.ai)
• PNG形式 (.png)
補足説明
この手のコンペなどは弊社は慣れておりませんので、ご質問ございましたらお気軽にご連絡ください。
依頼公開後の追記内容
ご提出いただいているデザイナーの方には大変申し訳ございませんが、案件が少ないため、一週間だけ延長させていただきます。
■ 選んだ理由

社内会議で慎重に選んだ結果、過半数でtavrin様に支持が集まりました。南国感、高級感、ギフト感とどれをとっても申し分ないデザインかと存じます。こちらの意図をしっかりと汲んでくれたと実感できるデザインです。

■ 提案者全員のお礼・コメント

この度は多数のご提案誠にありがとうございます。どれも非常に優れたデザインでした。また定期的にデザイン提案のご依頼をさせていただきますので、何卒よろしくお願い申し上げます。

```html
<!DOCTYPE html>
<html lang="en">
<head>
<meta charset="UTF-8">
<title>Palm Sugar Package Front</title>
<link rel="stylesheet" href="https://fonts.googleapis.com/css2?family=Fira+Sans:wght@600;700;800&family=Noto+Sans+JP:wght@500&display=swap">
<style>
  :root {
    --leaf-dark: #1f5a12;
    --leaf-mid: #4f9a1c;
    --leaf-light: #b8e04a;
    --panel-bg: #e5f6f3;
    --heading-green: #1f5e40;
    --text-green: #1c4a34;
    --label-brown: #8b4a26;
    --label-text: #ffffff;
    --badge-bg: #0c0c0c;
    --badge-text: #7cc9ea;
    --flower-tone-1: #8a5a35;
    --flower-tone-2: #c79a6a;
    --sugar-tone-1: #a8682c;
    --sugar-tone-2: #d8b48a;
    --fruit-tone: #9aa070;
  }
  * { margin: 0; padding: 0; box-sizing: border-box; }
  html, body { width: 723px; height: 1200px; overflow: hidden; background: #ffffff; }
  .package-front {
    position: relative;
    width: 723px;
    height: 1200px;
    overflow: hidden;
    background: var(--panel-bg);
    font-family: "Fira Sans", Arial, sans-serif;
  }
  .leaf-photo {
    position: absolute;
    left: 0; top: 0;
    width: 723px; height: 494px;
    background:
      radial-gradient(ellipse at 15% 85%, var(--leaf-dark) 0%, transparent 55%),
      linear-gradient(160deg, var(--leaf-light) 0%, var(--leaf-mid) 45%, var(--leaf-dark) 100%);
  }
  .brand-badge {
    position: absolute;
    left: 212px; top: 133px;
    width: 300px; height: 212px;
    background: var(--badge-bg);
    display: flex;
    align-items: center;
    justify-content: center;
  }
  .brand-name {
    font-weight: 700;
    font-size: 56px;
    letter-spacing: 2px;
    color: var(--badge-text);
  }
  .tagline {
    position: absolute;
    left: 0; top: 490px;
    width: 723px;
    text-align: center;
    font-weight: 700;
    font-size: 38px;
    line-height: 46px;
    color: var(--text-green);
  }
  .product-name {
    position: absolute;
    left: 40px; top: 604px;
    font-weight: 800;
    font-size: 91px;
    line-height: 1;
    color: var(--heading-green);
  }
  .product-name-jp {
    position: absolute;
    left: 53px; top: 704px;
    width: 267px; height: 36px;
    background: var(--label-brown);
    color: var(--label-text);
    font-family: "Noto Sans JP", sans-serif;
    font-weight: 500;
    font-size: 22px;
    display: flex;
    align-items: center;
    justify-content: center;
    letter-spacing: 2px;
  }
  .product-description {
    position: absolute;
    left: 43px; top: 820px;
    font-weight: 700;
    font-size: 26px;
    line-height: 42px;
    white-space: nowrap;
    color: var(--text-green);
  }
  .origin {
    position: absolute;
    left: 43px; top: 1098px;
    font-weight: 700;
    font-size: 20px;
    color: var(--text-green);
  }
  .palm-flower-photo {
    position: absolute;
    left: 578px; top: 575px;
    width: 145px; height: 400px;
    border-radius: 60px 60px 10px 10px;
    background: linear-gradient(180deg, var(--flower-tone-2) 0%, var(--flower-tone-1) 100%);
  }
  .sugar-and-fruit-photo {
    position: absolute;
    left: 355px; top: 820px;
    width: 368px; height: 380px;
    clip-path: polygon(120px 0, 100% 0, 100% 100%, 0 100%, 0 170px, 60px 140px);
    background:
      radial-gradient(circle at 22% 75%, var(--sugar-tone-2) 0%, var(--sugar-tone-1) 30%, transparent 55%),
      radial-gradient(circle at 72% 35%, var(--fruit-tone) 0%, #6c6e48 65%);
  }
</style>
</head>
<body>
  <main class="package-front">
    <div class="leaf-photo" role="img" aria-label="Close-up photo of a fanned green palmyra palm leaf"></div>

    <div class="brand-badge">
      <span class="brand-name">Koravan</span>
    </div>

    <p class="tagline">This is 100% naturally derived food.</p>

    <div class="palm-flower-photo" role="img" aria-label="Photo of palmyra palm flower spikes"></div>
    <div class="sugar-and-fruit-photo" role="img" aria-label="Photo of round palm sugar cakes beside palmyra palm fruits"></div>

    <h1 class="product-name">PALM SUGAR</h1>
    <div class="product-name-jp">パームシュガー</div>

    <p class="product-description">This is extracted from dense<br>Palmyra palm trees’ flowers;<br>it is from mother nature.</p>

    <p class="origin">MADE IN VIETNAM</p>
  </main>
</body>
</html>
```